I want an upgrade / face-lift to the all the pages and sections of the current website at vorenta.net. I am a developer but not a designer.

The website layout does not need to stay the same. Only the text, buttons, links, etc, need to stay the same. Logo can also be changed or altered.

1) Header
* Logo
* Tagline - Friends of the Messianic Community in Israel
* Short explanation - Vorenta.net aggregates new links from 113 websites of the Messianic Community in Israel. Learn more
* Login button
* Language Links (or picker) - English, Hebrew, Chinese (this currently isn't on Vorenta.net)

2) Nav Bar - no dropdowns
* Newsfeed
* Israel Directory
* International Directory
* Product Directory
* Website Directory

3) Sidebar
* Text - Sign up to Vorenta.net to receive a weekly email of new articles and videos from the Messianic community in Israel.
* Sign up button
* Brixo Ads or other Ads

4) List of Newsfeed links - (this is the main content of the homepage. Note the links go to other websites. It's not blog entries)
* Image
* Link Title
* website
* author (optional)
* date
* short description of link (optional)

5) Directory (Israel, International, Product)
* Search / Filter Bar (left vertical or horizontal ???)
* title - Israel Directory
* # of results
* A-Z
Partial for each organization
* logo
* first line - Link Name
* second link - type, city, language, area
* number of views
* description

6) Website Directory - page that lists all the websites that we crawl and gather links.
* needs upgrade / facelift

7) Organization Profile Page - click on http://vorenta.net/shalev-gate-fellowship as an example.
* all details as in list of directory, plus
* Meeting details
* contact details
* Donation details
* Donation link more prominent

8) Register Page
* include all details as on http://vorenta.net/register

9) Login Page
* include all details as on http://vorenta.net/login

10) About / FAQ / Contact pages
* include all details as on http://vorenta.net/about
* include all details as on http://vorenta.net/faq
* include all details as on http://vorenta.net/contact

11) Footer
* * include all details as on as website
About | Newsfeed | Israel Directory | International Directory | Product Directory | Website Directory | Contact
©2006–2013 Vorenta.net All rights reserved
Vorenta is a Hebrew word that means "community" or "congregation"

12) Bonus - Email Newsletter Design
* I want to send out 5 -10 new newsfeed links each weeks
* It should be similar to the newsfeed page, but for e-newsletters. I read that the css must for different and tables are preferred about for email.

The following pages appear for logged in users only
13) List of Ads
14) List of Events
15) Ad Single Page
16) Event Single Page
17) Edit Ad Form
18) Edit Event Form
19) Edit Organization Form
20) Edit User Information Form

Reason: First project. I originally entered 2 days, but am extending to 10 days.

I removed the requirement to delivery HTML/CSS and I static design of all pages is acceptable to win the project.  This is my first project and I wasn't aware that PixelHarbor focuses on static design and not HTML/CSS code.

Every designer essentially used the exact same "layout" that I currently have at vorenta.net and gave it a small "facelift".  I guess my wording in the brief of the word 'facelift' was not totally accurate.  The navbar / header layout does not need to stay the same.  I would appreciate to see different options such as the navbar at the top (like www.trendolix.net) or all one color on the header (like www.gbx.net) or making the logo all white and putting it inside the blue navbar (like trendolix.net).  Just some ideas that I had.

I am willing to make the project guaranteed but most of the designs are very close to what I have now.  

Note, any ideas / graphics / images / icons that show the visitor that the website is related to Israel would be helpful.

Reason: Not enough designs received

The project is now guaranteed‎.  I hope this encourages more designers to submit and to be creative.  I look forward to seeing more designs.

I'm interested in having a background on the left and right sides for larger screens.  For an example, see http://fieldsidetally.net/

I would like to have a faded image of the Israeli flag or a creative variation of it.

This website has a background image on the right-left sides that fades as you go down

I'm looking to use the space and the right-left to give the user at a quick glance that the website deals with Israel, community, Messianic/Christian, etc.

Another style that looks good is that white/gray such as http://www.filmquillnotes.net/ and https://vestly.io/

I'm interested to see how to block out difference sections with small color variations.

Reason: some designers request that I extend since they just accepted invitation

Another design that I like.  http://gigbarn.net/

Important change.  I want the newsfeed to look like a newsfeed. Right now, it looks like a blog site.  It's not obvious that articles are from other websites in the community.  I uploaded on the brief of clipvane's feed.  It shows the a small thumbnail (16x16 or 32x32) and then user name (it my case organization name or website name) on the upper left corner above the main image. 

On the header on want to change the wording on order.  

Top row -
Vorenta (logo in big) means community in Hebrew (in small letters) 

Next row (different background color)
The Messianic Community in Israel

Next row (different background color and smaller font)
Vorenta.net aggregates new links from 100+ websites of the Messianic Community in Israel. Learn more

I uploaded a jpg file with a new header rather than what is currently on vorenta.net

Target Market(s)

Christian around the world who love Israel

Industry/Entity Type

Events

Requirements
Must have
• responsive design to be readable on mobile devices
white / gray / blue theme
Zapto-style / portal website
Nice to have
• Bootstrap 3 of Foundation
Flat-UI (also not necessary, but I like it)
Graphics, icons, etcs, related to Israel
Passion, excellence, effort and attention to details :-)
Should not have
• dark background
too much fanciness or animations

```html
<!DOCTYPE html>
<html lang="en">
<head>
<meta charset="utf-8">
<title>Vorenta.net – Friends of the Messianic Community in Israel</title>
<link href="https://fonts.googleapis.com/css2?family=Roboto:ital,wght@0,400;0,500;0,700;1,400;1,700&family=Open+Sans:ital,wght@0,400;0,600;1,400&display=swap" rel="stylesheet">
<style>
:root{
  --page-bg:#ffffff;
  --frame:#e4e4e4;
  --blue:#1b6493;
  --blue-dark:#14527c;
  --navy:#2a2f6b;
  --link-blue:#1a5f95;
  --title-navy:#22285a;
  --red:#b81d1d;
  --orange:#e0750c;
  --green:#5aac1a;
  --panel:#f3f3f3;
  --panel-dark:#333333;
  --text:#333333;
  --footer:#3b3b3b;
  --photo-warm:#8d7c6d;
  --photo-cool:#7d8892;
}
*{box-sizing:border-box;margin:0;padding:0}
html,body{width:928px;height:1200px;overflow:hidden}
body{position:relative;background:var(--page-bg);font-family:'Open Sans',sans-serif;color:var(--text)}
a{text-decoration:none;color:inherit}
.abs{position:absolute}
.page-frame{left:50px;top:0;width:828px;height:1111px;border-left:1px solid var(--frame);border-right:1px solid var(--frame)}
.header-band{left:0;top:0;width:928px;height:92px;background:linear-gradient(#ffffff,#f1f1f1);border-bottom:1px solid #e2e2e2}
.language{right:62px;top:9px;font:400 10px 'Roboto',sans-serif;color:#444;display:flex;align-items:center;gap:4px}
.language .current{color:var(--link-blue)}
.flag{width:14px;height:9px;background:linear-gradient(#c8102e 0 0) center/100% 2px no-repeat,linear-gradient(#c8102e 0 0) center/2px 100% no-repeat,#1f3c88}
.caret{width:0;height:0;border:4px solid transparent;border-top-color:#666;margin-top:4px}
.brand{left:61px;top:33px;font:700 25px 'Roboto',sans-serif;color:var(--blue);letter-spacing:-.5px}
.tagline{left:250px;top:42px;font:italic 700 14px 'Roboto',sans-serif;color:#333}
.login{left:796px;top:40px;width:71px;height:23px;background:var(--green);border-radius:2px;color:#fff;font:500 11px 'Roboto',sans-serif;display:flex;align-items:center;justify-content:center;gap:8px}
.login svg{fill:#fff}
.main-nav{left:61px;top:72px;width:806px;height:38px;background:linear-gradient(var(--blue),var(--blue-dark));border-radius:3px 3px 0 0;display:flex;font:500 10px 'Roboto',sans-serif;color:#fff}
.main-nav a{display:flex;align-items:center;padding:0 15px}
.main-nav a.active{background:var(--navy);width:84px;justify-content:center;border-radius:3px 0 0 0;padding:0}
.intro{left:71px;top:118px;font:500 13px 'Roboto',sans-serif;color:#333}
.intro .count{color:var(--red)}
.intro .more{font:italic 400 10px 'Roboto',sans-serif;color:var(--red)}
.slider{left:62px;top:142px;width:615px;height:192px;border:2px solid #ddd;background:#fff}
.slide-photo{position:absolute;left:201px;top:0;right:0;bottom:0;background:linear-gradient(110deg,var(--photo-warm),#5b4e46 45%,var(--photo-cool))}
.slide-copy{position:absolute;left:0;top:0;width:230px;height:100%;background:linear-gradient(90deg,#fff 0,#fff 75%,rgba(255,255,255,0));padding:12px 12px}
.slide-copy h2{font:400 17px 'Roboto',sans-serif;color:var(--link-blue);margin-bottom:6px}
.slide-copy p{font-size:8.6px;line-height:13.5px;width:180px;color:#222}
.read-more{font:italic 400 9px/12px 'Roboto',sans-serif;color:var(--red)}
.block{display:block}
.slide-copy .read-more{margin-top:3px}
.slide-meta{margin-top:8px;font:italic 400 8px 'Roboto',sans-serif;display:flex;flex-direction:column;gap:4px}
.slide-meta span{display:flex;align-items:center;gap:8px;height:12px}
.site{color:var(--link-blue)}
.author{color:#555}
.date{color:var(--orange)}
.slide-arrows{display:flex;gap:10px;margin-top:17px}
.signup{left:691px;top:115px;width:176px;height:220px;background:var(--panel-dark);color:#fff;padding:10px 12px}
.signup p{font:500 9.6px/15.5px 'Roboto',sans-serif}
.signup label{display:block;font:400 9.5px 'Roboto',sans-serif;margin:19px 0 6px}
.field{height:21px;background:#f5f5f5;border-radius:2px;font:italic 400 8px 'Roboto',sans-serif;color:#888;display:flex;align-items:center;padding:0 7px;justify-content:space-between}
.field+.field{margin-top:11px}
.btn-signup{margin:14px 0 0 80px;width:71px;height:24px;background:var(--orange);border-radius:2px;color:#fff;font:500 10.5px 'Roboto',sans-serif;display:flex;align-items:center;justify-content:center}
.feeds{left:62px;top:347px;width:615px;height:753px;background:var(--panel);padding:11px 11px}
.feeds h1{font:400 16px 'Roboto',sans-serif;color:var(--blue);margin-bottom:12px}
.feed-item{position:relative;background:#fff;border:1px solid #d8d8d8;height:118px;margin-bottom:13px;padding:13px 14px 0 154px}
.feed-thumb{position:absolute;left:15px;top:15px;width:124px;height:87px;border:2px solid #ddd}
.feed-item h3{font:500 12px 'Roboto',sans-serif;color:var(--title-navy);margin-bottom:4px}
.meta{display:flex;align-items:center;gap:6px;font:italic 400 7.6px 'Roboto',sans-serif;margin-bottom:5px}
.meta .sep{color:#999}
.meta .ic{display:flex;align-items:center;gap:6px}
.feed-item p{font-size:8.9px;line-height:14px;color:#333;margin-bottom:9px}
.play-mark{width:22px;height:22px;border-radius:50%;background:rgba(0,0,0,.45);display:flex;align-items:center;justify-content:center}
.pager{position:absolute;left:11px;right:11px;top:709px;display:flex;justify-content:space-between}
.pager a{height:27px;background:var(--blue);color:#fff;font:500 9.5px 'Roboto',sans-serif;display:flex;align-items:center;padding:0 10px;border-radius:2px}
.ads{left:691px;top:347px;width:176px;height:753px;background:var(--panel)}
.ads-label{position:absolute;top:11px;width:100%;text-align:center;font:400 8px 'Roboto',sans-serif;color:#999}
.ad{position:absolute;left:34px;width:109px;background:#fff;border:1px solid #ccc;padding:22px 0 0 2px}
.ad .choice{position:absolute;right:3px;top:2px;width:0;height:0;border:4px solid transparent;border-left:6px solid #3a8ed0}
.ad h4{font:400 15px 'Open Sans',sans-serif;color:var(--blue);line-height:18px}
.ad .url{font-size:9.5px;color:#0a7a3c;margin:2px 0 12px}
.ad p{font-size:11.5px;line-height:13px;color:#666}
.ad .go{margin:12px 0 0 40px;width:23px;height:23px;border-radius:50%;background:#2a6b8e;display:flex;align-items:center;justify-content:center}
.footer{left:0;top:1111px;width:928px;height:89px;background:var(--footer);color:#ddd}
.footer-links{position:absolute;left:62px;top:19px;font:400 8.5px 'Roboto',sans-serif;display:flex;gap:9px}
.footer-links i{font-style:normal;color:#888}
.copyright{position:absolute;left:62px;top:48px;font:400 7.5px 'Roboto',sans-serif;color:#bbb}
.copyright b{color:#fff}
.footer-note{position:absolute;left:62px;top:63px;font:400 8px 'Roboto',sans-serif}
.social{position:absolute;left:718px;top:34px;display:flex;gap:6px}
.social span{width:21px;height:21px;background:#4b47c8;border-radius:2px}
</style>
</head>
<body>
<svg width="0" height="0" style="position:absolute">
  <defs>
    <symbol id="i-globe" viewBox="0 0 12 12"><circle cx="6" cy="6" r="5.3" fill="none" stroke="#666" stroke-width="1.2"/><path d="M1 6h10M6 1c-2.5 3-2.5 7 0 10M6 1c2.5 3 2.5 7 0 10" fill="none" stroke="#666" stroke-width=".9"/></symbol>
    <symbol id="i-user" viewBox="0 0 12 12"><circle cx="6" cy="3.5" r="2.7"/><path d="M1 12c0-4 2-5.5 5-5.5s5 1.5 5 5.5z"/></symbol>
    <symbol id="i-cal" viewBox="0 0 12 12"><rect x="1" y="2" width="10" height="9.5" fill="none" stroke="#666" stroke-width="1.2"/><rect x="1" y="2" width="10" height="2.5" fill="#666"/><rect x="3" y="6" width="2" height="2" fill="#666"/><rect x="6.5" y="6" width="2" height="2" fill="#666"/></symbol>
  </defs>
</svg>

<div class="abs header-band"></div>
<div class="abs page-frame"></div>

<div class="abs language">Select Language : <span class="flag"></span><span class="current">English</span><span class="caret"></span></div>
<a class="abs brand" href="#">Vorenta</a>
<div class="abs tagline">Friends of the Messianic Community in Israel</div>
<a class="abs login" href="#"><svg width="11" height="11"><use href="#i-user"/></svg>LOG IN</a>

<nav class="abs main-nav">
  <a class="active" href="#">NEWSFEED</a>
  <a href="#">ISRAEL DIRECTORY</a>
  <a href="#">INTERNATIONAL DIRECTORY</a>
  <a href="#">PRODUCT DIRECTORY</a>
  <a href="#">WEBSITE DIRECTORY</a>
</nav>

<div class="abs intro">Vorenta.net Aggregates new links from <span class="count">113 websites</span> of the Messianic Community in Israel.... <a class="more" href="#">Learn more</a></div>

<section class="abs slider">
  <div class="slide-photo" role="img" aria-label="Photo of worshippers gathered outdoors during the Days of Awe"></div>
  <div class="slide-copy">
    <h2>Living in Israel Blog</h2>
    <p>The past 10 Days of Awe conclude today with Yom Kippur (Day of Atonement), the holiest day of the Jewish calendar.</p>
    <a class="read-more block" href="#">Read More</a>
    <div class="slide-meta">
      <span class="site"><svg width="11" height="11"><use href="#i-globe"/></svg>cedarlineblog.net</span>
      <span class="author"><svg width="11" height="11" fill="#666"><use href="#i-user"/></svg>Dalia Verhoen-Ashby</span>
      <span class="date"><svg width="11" height="11"><use href="#i-cal"/></svg>September 21, 2013</span>
    </div>
    <div class="slide-arrows">
      <svg width="10" height="14" viewBox="0 0 10 14"><path d="M7 2L2 7l5 5" fill="none" stroke="#222" stroke-width="2"/></svg>
      <svg width="10" height="14" viewBox="0 0 10 14"><path d="M3 2l5 5-5 5" fill="none" stroke="#222" stroke-width="2"/></svg>
    </div>
  </div>
</section>

<aside class="abs signup">
  <p>Sign up to Vorenta.net to receive a weekly email that aggregates updates from 113 websites of the Messianic community in Israel.</p>
  <label>Email</label>
  <div class="field">Enter Email</div>
  <div class="field">Select Country <svg width="11" height="6"><path d="M0 0h11L5.5 6z" fill="#777"/></svg></div>
  <a class="btn-signup" href="#">SIGN UP</a>
</aside>

<main class="abs feeds">
  <h1>NEWS FEEDS</h1>

  <article class="feed-item">
    <div class="feed-thumb" role="img" aria-label="Photo of a family at a holiday dinner table" style="background:linear-gradient(135deg,#c9b6a0,#8a6d5a)"></div>
    <h3>Living in Israel Blog: High Holidays, Modern Israeli Style</h3>
    <div class="meta"><span class="ic site"><svg width="11" height="11"><use href="#i-globe"/></svg>cedarlineblog.net</span><span class="sep">|</span><span class="ic author"><svg width="11" height="11" fill="#666"><use href="#i-user"/></svg>Dalia Verhoen-Ashby</span><span class="sep">|</span><span class="ic date"><svg width="11" height="11"><use href="#i-cal"/></svg>September 21, 2013</span></div>
    <p>A digest of the holidays in bite size pieces allowing people to enjoy as well as understand the purpose of each special day.</p>
    <a class="read-more block" href="#">Read More</a>
  </article>

  <article class="feed-item">
    <div class="feed-thumb" role="img" aria-label="Video still of palm branches on a sukkah" style="background:linear-gradient(135deg,#6f7458,#b9b7a2);display:flex;align-items:center;justify-content:center"><span class="play-mark"><svg width="8" height="9"><path d="M1 0l7 4.5L1 9z" fill="#fff"/></svg></span></div>
    <h3>Sukkot 5774: Build Your Booth and Dwell in It</h3>
    <div class="meta"><span class="ic site"><svg width="11" height="11"><use href="#i-globe"/></svg>cedarlineblog.net</span><span class="sep">|</span><span class="ic author"><svg width="11" height="11" fill="#666"><use href="#i-user"/></svg>Dalia Verhoen-Ashby</span><span class="sep">|</span><span class="ic date"><svg width="11" height="11"><use href="#i-cal"/></svg>September 21, 2013</span></div>
    <p>The day after Yom Kippur all across Israel sounds of hammering lets us know it's almost time for Sukkot – Feast of Tabernacles.</p>
    <a class="read-more block" href="#">Read More</a>
  </article>

  <article class="feed-item">
    <div class="feed-thumb" role="img" aria-label="Television broadcast still of a preacher" style="background:linear-gradient(#1d3fa0 0,#2a55c0 70%,#111 70%)"></div>
    <h3>Why didn't I Name Names?</h3>
    <div class="meta"><span class="ic site"><svg width="11" height="11"><use href="#i-globe"/></svg>cedarlineblog.net</span><span class="sep">|</span><span class="ic author"><svg width="11" height="11" fill="#666"><use href="#i-user"/></svg>Dalia Verhoen-Ashby</span><span class="sep">|</span><span class="ic date"><svg width="11" height="11"><use href="#i-cal"/></svg>September 21, 2013</span></div>
    <p>The response to my blog earlier this week has been encouraging. Truthfully I suspected it would strike a chord inside of those who are tired of listening to wealthy preachers make false promises of blessing and prosperity......<a class="read-more" href="#">Read More</a></p>
  </article>

  <article class="feed-item">
    <div class="feed-thumb" role="img" aria-label="Photo of volunteers sorting donated clothes" style="background:linear-gradient(135deg,#cfd3d6,#6d7680)"></div>
    <h3>Time to Start Sorting</h3>
    <div class="meta"><span class="ic site"><svg width="11" height="11"><use href="#i-globe"/></svg>cedarlineblog.net</span><span class="sep">|</span><span class="ic author"><svg width="11" height="11" fill="#666"><use href="#i-user"/></svg>Dalia Verhoen-Ashby</span><span class="sep">|</span><span class="ic date"><svg width="11" height="11"><use href="#i-cal"/></svg>September 21, 2013</span></div>
    <p>This past Monday a small group of volunteers got together to begin sorting clothes for the upcoming distribution center, and what a job it turned out to be!</p>
    <a class="read-more block" href="#">Read More</a>
  </article>

  <article class="feed-item">
    <div class="feed-thumb" role="img" aria-label="Podcast episode cover artwork" style="background:linear-gradient(135deg,#c9a13c,#6fa3c0)"></div>
    <h3>[Podcast] Yom Kippur, Televangelists and Syria Update</h3>
    <div class="meta"><span class="ic site"><svg width="11" height="11"><use href="#i-globe"/></svg>cedarlineblog.net</span><span class="sep">|</span><span class="ic author"><svg width="11" height="11" fill="#666"><use href="#i-user"/></svg>Dalia Verhoen-Ashby</span><span class="sep">|</span><span class="ic date"><svg width="11" height="11"><use href="#i-cal"/></svg>September 21, 2013</span></div>
    <p>Eli Marnot and the Cedarline Media team are back with the 30th episode of the Cedarline Israel Report Podcast!</p>
    <a class="read-more block" href="#">Read More</a>
  </article>

  <div class="pager">
    <a href="#">PREVIOUS NEWS FEEDS</a>
    <a href="#">MORE NEWS FEEDS</a>
  </div>
</main>

<aside class="abs ads">
  <div class="ads-label">3rd Party Ads</div>
  <div class="ad" style="top:23px;height:358px">
    <span class="choice"></span>
    <h4>NameKettle® - Official Site</h4>
    <div class="url">in.namekettle.net</div>
    <p>Rs 109 Limited Time .COM Sale Register Your Domain Now!</p>
    <div class="go"><svg width="9" height="11"><path d="M2 1l5 4.5L2 10" fill="none" stroke="#fff" stroke-width="2"/></svg></div>
  </div>
  <div class="ad" style="top:389px;height:345px">
    <span class="choice"></span>
    <h4>NameKettle® - Official Site</h4>
    <div class="url">in.namekettle.net</div>
    <p>Rs 109 Limited Time .COM Sale Register Your Domain Now!</p>
    <div class="go"><svg width="9" height="11"><path d="M2 1l5 4.5L2 10" fill="none" stroke="#fff" stroke-width="2"/></svg></div>
  </div>
</aside>

<footer class="abs footer">
  <nav class="footer-links">
    <a href="#">About</a><i>|</i><a href="#">Newsfeed</a><i>|</i><a href="#">Israel Directory</a><i>|</i><a href="#">International Directory</a><i>|</i><a href="#">Product Directory</a><i>|</i><a href="#">Website Directory</a><i>|</i><a href="#">Contact</a>
  </nav>
  <div class="copyright">©2006–2013 <b>Vorenta.net</b> All rights reserved</div>
  <div class="footer-note">Vorenta is a Hebrew word that means "community" or "congregation"</div>
  <div class="social" aria-label="Social links"><span></span><span></span><span></span><span></span></div>
</footer>
</body>
</html>
```